Car Detailing product label for 750ML Clear Bottle

I need a label for various product with differente color for each products but in the same size bottle each time. It's only for our purpose no commercial application. I need a template with differente color but same design. The name for product it's : Tidal Quartz. We dont have any logo because it's only for us. We like like car silhouette in the logo or in background or something like that.

And for the product we have many like : APC Cleaner, Drying Aid, Wheel Cleaner and some other.

```html
<!DOCTYPE html>
<html lang="en">
<head>
<meta charset="utf-8">
<title>Tidal Quartz – APC All Perpose Cleaner label</title>
<link rel="stylesheet" href="https://fonts.googleapis.com/css2?family=Anton&family=Barlow+Condensed:wght@500&family=Montserrat:ital,wght@0,600;1,800&display=swap">
<style>
  :root {
    --page-bg: #ececec;
    --label-dark: #1b1b1d;
    --label-dark-soft: #2a2a2d;
    --accent-red: #ef2f3c;
    --headline-red: #d81f2c;
    --headline-outline: #f4f4f4;
    --tagline-grey: #9a9a9c;
    --white: #ffffff;
  }
  * { margin: 0; padding: 0; box-sizing: border-box; }
  html, body {
    width: 1200px;
    height: 2385px;
    overflow: hidden;
    background: var(--page-bg);
  }
  .label {
    position: absolute;
    left: 120px;
    top: 343px;
    width: 960px;
    height: 1699px;
    overflow: hidden;
    background: var(--label-dark);
  }
  .label-texture {
    position: absolute;
    inset: 0;
    background: radial-gradient(ellipse at 50% 45%, var(--label-dark-soft) 0%, var(--label-dark) 75%);
  }
  .label-stripes {
    position: absolute;
    inset: 0;
    width: 100%;
    height: 100%;
  }
  .brand-name {
    position: absolute;
    left: 80px;
    top: 250px;
    font-family: "Montserrat", sans-serif;
    font-weight: 600;
    font-size: 56px;
    color: var(--accent-red);
    letter-spacing: 0.5px;
  }
  .headline {
    position: absolute;
    left: 0;
    top: 580px;
    width: 960px;
    text-align: center;
    transform: rotate(-9deg);
    font-family: "Anton", sans-serif;
    color: var(--headline-red);
    -webkit-text-stroke: 4px var(--headline-outline);
    paint-order: stroke fill;
    text-shadow: 0 6px 8px rgba(0,0,0,0.55);
    line-height: 0.98;
  }
  .headline-code { display: block; font-size: 170px; margin-left: -40px; }
  .headline-name { display: block; font-size: 112px; margin-left: 20px; }
  .headline-name + .headline-name { margin-left: -20px; }
  .tagline {
    position: absolute;
    left: 372px;
    top: 1250px;
    transform: rotate(-12deg);
    transform-origin: left top;
    font-family: "Barlow Condensed", sans-serif;
    font-weight: 500;
    font-size: 90px;
    line-height: 0.92;
    color: var(--tagline-grey);
    text-align: center;
  }
  .volume {
    position: absolute;
    right: 50px;
    bottom: 58px;
    font-family: "Montserrat", sans-serif;
    font-weight: 800;
    font-style: italic;
    font-size: 54px;
    color: var(--white);
  }
</style>
</head>
<body>
  <main class="label">
    <div class="label-texture" role="img" aria-label="Dark label background with a subtle dotted carbon texture"></div>

    <svg class="label-stripes" viewBox="0 0 390 690" preserveAspectRatio="none" aria-hidden="true">
      <g fill="var(--accent-red)">
        <!-- upper stripe group -->
        <polygon points="300,112 390,82 390,95 300,125"/>
        <polygon points="258,128 270,100 278,100 266,128"/>
        <polygon points="272,128 284,100 292,100 280,128"/>
        <polygon points="286,128 298,100 306,100 294,128"/>
        <!-- lower stripe group -->
        <polygon points="0,548 70,528 70,541 0,561"/>
        <polygon points="62,566 74,536 82,536 70,566"/>
        <polygon points="78,566 90,536 98,536 86,566"/>
        <polygon points="94,566 106,536 114,536 102,566"/>
        <!-- volume tab -->
        <polygon points="208,690 230,640 390,630 390,690"/>
      </g>
      <g stroke="var(--accent-red)" stroke-linecap="round" fill="none" stroke-width="5">
        <line x1="0" y1="200" x2="235" y2="152"/>
        <line x1="0" y1="238" x2="390" y2="130"/>
        <line x1="148" y1="492" x2="392" y2="424"/>
      </g>
    </svg>

    <div class="brand-name">Tidal Quartz</div>

    <h1 class="headline">
      <span class="headline-code">APC</span>
      <span class="headline-name">ALL PERPOSE</span>
      <span class="headline-name">CLEANER</span>
    </h1>

    <p class="tagline">MORE THAN<br>DETALING</p>

    <div class="volume">750ml</div>
  </main>
</body>
</html>
```